Veterinary Practice

This is a large and small animal practice that primarily treats cattle,horses,dog and cats. I desire a business card with a picture of each of those animals. I prefer a black cow but the other animals can be any color. The back of the cards needs to have appointment scheduling information.

Industry/Entity Type

Business

Contact Information for Business Card

Copper Ridge Veterinary Services
Daniel M Petterby DVM
3847 S Highway 41
Linden Falls KS 66520
785-312-9048

```html
<!DOCTYPE html>
<html lang="en">
<head>
<meta charset="utf-8">
<title>Copper Ridge Veterinary Services – Business Card</title>
<link rel="stylesheet" href="https://fonts.googleapis.com/css2?family=Cinzel:wght@600&family=Open+Sans:wght@400;600;700&display=swap">
<style>
  :root {
    --green: #2f8a3a;
    --green-dark: #1f6b2a;
    --black: #141414;
    --paper: #ffffff;
    --paper-shade: #f1f2f1;
    --backdrop: #d9dbda;
    --rule: #c9ccca;
    --ink-light: #e8e8e8;
  }
  * { box-sizing: border-box; margin: 0; padding: 0; }
  html, body { width: 885px; height: 1200px; overflow: hidden; }
  body {
    background: var(--backdrop);
    display: flex;
    flex-direction: column;
    align-items: center;
    justify-content: center;
    gap: 70px;
    font-family: "Open Sans", sans-serif;
  }
  .card {
    position: relative;
    width: 760px;
    height: 434px;
    background: linear-gradient(180deg, var(--paper), var(--paper-shade));
    box-shadow: 0 10px 26px rgba(0,0,0,0.22);
    overflow: hidden;
  }

  /* Front */
  .front .brand {
    position: absolute;
    top: 44px; left: 0; right: 0;
    display: flex; flex-direction: column; align-items: center;
  }
  .brand-mark {
    width: 118px; height: 118px;
    background: var(--green);
    border-radius: 10px;
    margin-bottom: 18px;
  }
  .brand-name {
    font-family: "Cinzel", serif;
    font-weight: 600;
    color: var(--green-dark);
    text-align: center;
    line-height: 1.1;
  }
  .brand-name .line-1 { display: block; font-size: 46px; letter-spacing: 1px; }
  .brand-name .line-2 { display: block; font-size: 22px; letter-spacing: 2px; margin-top: 4px; }
  .front-band {
    position: absolute; left: 0; right: 0; bottom: 0;
    height: 54px; background: var(--black);
    border-top: 8px solid var(--green);
  }

  /* Back */
  .back .practice {
    position: absolute; top: 28px; left: 34px;
    font-family: "Cinzel", serif; font-weight: 600;
    color: var(--green-dark); line-height: 1.1;
  }
  .back .practice .line-1 { display: block; font-size: 26px; }
  .back .practice .line-2 { display: block; font-size: 13px; letter-spacing: 1.5px; margin-top: 2px; }
  .appointment-label {
    position: absolute; top: 112px; left: 34px;
    font-size: 14px; font-weight: 700; letter-spacing: 1px; color: var(--black);
  }
  .schedule {
    position: absolute; top: 140px; left: 34px;
    width: 470px; height: 262px;
    display: grid; grid-template-columns: repeat(6, 1fr); gap: 8px;
  }
  .day {
    display: flex; flex-direction: column;
    border: 1px solid var(--rule);
    background: var(--paper);
  }
  .day-slot { flex: 1; }
  .day-name {
    height: 42px; background: var(--green);
    color: var(--paper); font-size: 12px; font-weight: 700;
    display: flex; align-items: center; justify-content: center; letter-spacing: 1px;
  }
  .contact-panel {
    position: absolute; top: 0; right: 0; bottom: 0;
    width: 200px; background: var(--black);
    border-left: 10px solid var(--green);
  }
  .contact {
    position: absolute; top: 50%; left: 50%;
    width: 380px;
    transform: translate(-50%, -50%) rotate(-90deg);
    color: var(--ink-light); text-align: center;
    font-size: 16px; line-height: 1.55;
  }
  .contact .doctor { font-weight: 700; font-size: 18px; color: var(--paper); }
  .contact .phone { font-weight: 600; color: var(--green); margin-top: 6px; }
</style>
</head>
<body>

  <section class="card front" aria-label="Card front">
    <div class="brand">
      <div class="brand-mark"></div>
      <p class="brand-name">
        <span class="line-1">Copper Ridge</span>
        <span class="line-2">Veterinary Services</span>
      </p>
    </div>
    <div class="front-band"></div>
  </section>

  <section class="card back" aria-label="Card back">
    <p class="practice">
      <span class="line-1">Copper Ridge</span>
      <span class="line-2">Veterinary Services</span>
    </p>
    <p class="appointment-label">APPOINTMENT TIME/NAME</p>
    <div class="schedule">
      <div class="day"><div class="day-slot"></div><div class="day-name">MON</div></div>
      <div class="day"><div class="day-slot"></div><div class="day-name">TUE</div></div>
      <div class="day"><div class="day-slot"></div><div class="day-name">WED</div></div>
      <div class="day"><div class="day-slot"></div><div class="day-name">THU</div></div>
      <div class="day"><div class="day-slot"></div><div class="day-name">FRI</div></div>
      <div class="day"><div class="day-slot"></div><div class="day-name">SAT</div></div>
    </div>
    <div class="contact-panel">
      <div class="contact">
        <p class="doctor">Daniel M Petterby DVM</p>
        <p>3847 S Highway 41</p>
        <p>Linden Falls KS 66520</p>
        <p class="phone">785-312-9048</p>
      </div>
    </div>
  </section>

</body>
</html>
```